Real Estate Company Looking for Business Card Designs for 3 Executives

Hello!
Thanks so much for considering our project! We are a real estate investment company located in Edmonton, Alberta called Bellcrane Group of Companies. We invest/develop both commercial and residential real estate and are looking to create 3 DOUBLE-SIDED business cards for 3 top executives in the company! (for some reason it won't let us select the double-sided option, but yes, the cards are double sided and would be happy to tip extra)

We have certain guidelines that we want our business cards to for sure follow - the back of the Business card has to be the Black Background Version of the Logo which has already been designed and linked as a file (first file). We want the entire back of the card to simply just be the black background logo. In terms of the front of the card, would like to see a smaller version of the white background logo (linked as the second file) in the top left hand corner - of course, feel free to get creative and we can make revisions together along the way! and Then after that, just text. We want the card to be sharp, clean, easy on the eyes and highly professional looking. We would like the card to include the Full name of the Company (Bellcrane Group of Companies), Name of the Person, Title, Phone, Email. If possible please provide the front part of the card for 3 people:

1) Bellcrane Group of Companies, Nora Lindqvist, Chief Financial Officer, 780-555-0142, noralindqvist@bellcranegroup.example

2) Bellcrane Group of Companies, Julien Lindqvist, Chief Executive Officer, 780-555-0187, julienlindqvist@bellcranegroup.example

3) Bellcrane Group of Companies, Tom Okafor, Chief Operations Officer, 587-555-0163, tomokafor@bellcranegroup.example

Thank you so much for considering our project & we look forward to seeing your designs!

```html
<!DOCTYPE html>
<html lang="en">
<head>
<meta charset="utf-8">
<title>Bellcrane – Business Card</title>
<link href="https://fonts.googleapis.com/css2?family=Arimo:wght@400;700&display=swap" rel="stylesheet">
<style>
  :root {
    --stage: #2b2b2b;
    --card-black: #0b0809;
    --card-white: #ffffff;
    --ink: #141414;
    --paper-ink: #f4f8fa;
    --rule: #2a2a2a;
    --tree-dark: #1a1617;
    --tree-light: #e9e9e9;
  }
  * { box-sizing: border-box; margin: 0; padding: 0; }
  html, body {
    width: 1200px; height: 1015px; overflow: hidden;
    background: var(--stage);
    font-family: "Arimo", Arial, sans-serif;
  }
  .stage { position: relative; width: 1200px; height: 1015px; }

  .card {
    position: absolute; width: 700px; height: 400px;
    box-shadow: 0 10px 30px rgba(0,0,0,.45);
    overflow: hidden;
  }

  /* Back of card */
  .card--back { left: 60px; top: 70px; background: var(--card-black); }
  .card--back .forest {
    position: absolute; right: 70px; top: 0; width: 220px; height: 100%;
    background: linear-gradient(90deg, var(--card-black), var(--tree-dark) 40%, var(--tree-dark) 70%, var(--card-black));
  }
  .wordmark {
    position: absolute; display: flex; align-items: center; gap: 14px;
    font-weight: 400; letter-spacing: 10px; font-size: 30px;
  }
  .wordmark .mark-dot { width: 14px; height: 14px; border-radius: 50%; background: currentColor; }
  .card--back .wordmark { left: 150px; top: 180px; color: var(--paper-ink); }

  /* Front of card */
  .card--front { left: 440px; top: 540px; background: var(--card-white); color: var(--ink); }
  .card--front .forest {
    position: absolute; left: 50px; top: 0; width: 150px; height: 100%;
    background: linear-gradient(90deg, #fff, var(--tree-light) 35%, var(--tree-light) 65%, #fff);
  }
  .card--front .wordmark { right: 60px; top: 70px; color: var(--ink); font-size: 28px; }
  .rule-top {
    position: absolute; left: 200px; right: 40px; top: 160px; border-top: 1.5px solid var(--rule);
  }
  .website { position: absolute; right: 40px; top: 180px; font-size: 17px; }
  .person { position: absolute; left: 40px; top: 240px; }
  .person__name { font-weight: 700; font-size: 22px; letter-spacing: .5px; }
  .person__title { font-size: 19px; margin-top: 2px; }
  .rule-bottom {
    position: absolute; left: 40px; width: 320px; top: 305px; border-top: 1.5px solid var(--rule);
  }
  .contacts { position: absolute; left: 40px; top: 318px; list-style: none; font-size: 20px; }
  .contacts li { display: flex; align-items: center; gap: 10px; height: 30px; }
  .contacts svg { width: 18px; height: 18px; fill: var(--ink); flex: none; }
</style>
</head>
<body>
<main class="stage">
  <section class="card card--back" aria-label="Card back">
    <div class="forest" role="img" aria-label="Dark silhouette of tall pine trees"></div>
    <div class="wordmark"><span class="mark-dot"></span>BELLCRANE</div>
  </section>

  <section class="card card--front" aria-label="Card front">
    <div class="forest" role="img" aria-label="Faint grey pine tree trunks"></div>
    <div class="wordmark"><span class="mark-dot"></span>BELLCRANE</div>
    <div class="rule-top"></div>
    <p class="website">www.bellcranegroup.example</p>
    <div class="person">
      <p class="person__name">TOM OKAFOR</p>
      <p class="person__title">Chief Operations Officer</p>
    </div>
    <div class="rule-bottom"></div>
    <ul class="contacts">
      <li>
        <svg viewBox="0 0 24 24" aria-hidden="true"><path d="M6.6 10.8a15.1 15.1 0 0 0 6.6 6.6l2.2-2.2a1 1 0 0 1 1-.25 11.4 11.4 0 0 0 3.6.57 1 1 0 0 1 1 1V20a1 1 0 0 1-1 1A17 17 0 0 1 3 4a1 1 0 0 1 1-1h3.5a1 1 0 0 1 1 1c0 1.25.2 2.45.57 3.57a1 1 0 0 1-.25 1z"/></svg>
        587-555-0163
      </li>
      <li>
        <svg viewBox="0 0 24 24" aria-hidden="true"><path d="M2 5h20v14H2zm2 2v.4l8 5.2 8-5.2V7zm0 2.8V17h16V9.8l-8 5.2z"/></svg>
        tomokafor@bellcranegroup.example
      </li>
    </ul>
  </section>
</main>
</body>
</html>
```